TGV Electricial Contracting Services

Hi guys, after a design for my small electrical company, have logo design files to be incorporated into the layout, the basic concept is electrical contracting services for residential, commercial, industrial & data services, image is clean clear and strong,

Card format is to have a nice clean logo on front,with maybe the Residential – commercial – industrial - data, followed with licensed & insured, followed by contact details on backside of the card.

Target Market(s)

Residential, commercial, industrial sectors.

Industry/Entity Type

Electrical

Contact Information for Business Card

TGV logo,
Residential – commercial – industrial - data
REC: 57310
Email: tgv@wavolink.net.au
Phone: 0472 358 129

Requirements
Must have
• Clean & strong design.
Nice to have
• If possible, I would like the logo colours inverted so the text is orange and the background is black on the front of the card, then the backside of the card be the reverse colour
Should not have
• No Sparks, lightning bolts,

```html
<!DOCTYPE html>
<html lang="en">
<head>
<meta charset="utf-8">
<title>Tyler Grant Voltworks – Business Cards</title>
<link href="https://fonts.googleapis.com/css2?family=Lato:wght@400;700;900&display=swap" rel="stylesheet">
<style>
  :root {
    --backdrop: #2b2b2d;
    --card: #f7f7f7;
    --ink: #1f1f23;
    --ink-soft: #5a5a5e;
    --band: #1e1e22;
    --band-text: #ffffff;
  }
  * { margin: 0; padding: 0; box-sizing: border-box; }
  html, body {
    width: 1200px; height: 873px; overflow: hidden;
    background: var(--backdrop);
    font-family: "Lato", sans-serif;
  }
  .card {
    position: absolute;
    width: 560px; height: 320px;
    background: var(--card);
    box-shadow: 0 12px 30px rgba(0,0,0,.45);
    overflow: hidden;
  }
  .card--front { left: 70px; top: 70px; }
  .card--back { left: 570px; top: 480px; }

  .wordmark { color: var(--ink); font-weight: 900; line-height: 1; }
  .wordmark__letters { display: block; letter-spacing: 2px; }
  .wordmark__name { display: block; letter-spacing: .5px; }

  .card--front .wordmark {
    position: absolute; top: 62px; left: 0; right: 0; text-align: center;
  }
  .card--front .wordmark__letters { font-size: 78px; }
  .card--front .wordmark__name { font-size: 16px; margin-top: 4px; }

  .front-tagline {
    position: absolute; top: 212px; left: 0; right: 0;
    text-align: center; color: var(--ink-soft);
    font-size: 17px; letter-spacing: 1px; line-height: 1.6;
  }

  .card--back .wordmark { position: absolute; left: 40px; top: 58px; }
  .card--back .wordmark__letters { font-size: 70px; }
  .card--back .wordmark__name { font-size: 15px; margin-top: 4px; }

  .divider {
    position: absolute; left: 300px; top: 34px;
    width: 2px; height: 130px; background: var(--ink);
  }
  .contact { position: absolute; left: 322px; top: 30px; color: var(--ink); }
  .contact__name { font-size: 24px; font-weight: 700; }
  .contact__role {
    font-size: 13px; color: var(--ink-soft); letter-spacing: 1px;
    margin: 2px 0 14px 58px;
  }
  .contact__list { list-style: none; font-size: 14px; line-height: 1.35; }
  .contact__list li { display: flex; align-items: flex-start; gap: 10px; margin-bottom: 4px; }
  .icon {
    flex: none; width: 18px; height: 18px; border-radius: 4px;
    background: var(--ink); display: flex; align-items: center; justify-content: center;
  }

  .services {
    position: absolute; left: 0; right: 0; bottom: 32px;
  }
  .services__rule { height: 3px; background: var(--band); margin: 6px 0; }
  .services__band {
    background: var(--band); color: var(--band-text);
    font-weight: 700; font-size: 15px; text-align: center;
    padding: 10px 12px; line-height: 1.5; letter-spacing: .3px;
  }
</style>
</head>
<body>

<section class="card card--front" aria-label="Business card front">
  <div class="wordmark">
    <span class="wordmark__letters">TGV</span>
    <span class="wordmark__name">Tyler Grant Voltworks</span>
  </div>
  <p class="front-tagline">
    LICENCED &amp; INSURED<br>
    RESIDENTIAL - COMMERCIAL - INDUSTRIAL
  </p>
</section>

<section class="card card--back" aria-label="Business card back">
  <div class="wordmark">
    <span class="wordmark__letters">TGV</span>
    <span class="wordmark__name">Tyler Grant Voltworks</span>
  </div>

  <div class="divider"></div>

  <div class="contact">
    <p class="contact__name">Marco Delgado</p>
    <p class="contact__role">INCHARGE</p>
    <ul class="contact__list">
      <li>
        <span class="icon"><svg width="10" height="12" viewBox="0 0 10 12"><rect x="1.5" y="0.5" width="7" height="11" rx="1.2" fill="none" stroke="#fff" stroke-width="1.2"/><circle cx="5" cy="9.5" r=".8" fill="#fff"/></svg></span>
        <span>0472 358 129</span>
      </li>
      <li>
        <span class="icon"><svg width="12" height="9" viewBox="0 0 12 9"><rect x=".5" y=".5" width="11" height="8" fill="none" stroke="#fff" stroke-width="1.1"/><path d="M.5 .8 6 5 11.5 .8" fill="none" stroke="#fff" stroke-width="1.1"/></svg></span>
        <span>tgv@wavolink.net.au</span>
      </li>
      <li>
        <span class="icon"><svg width="10" height="12" viewBox="0 0 10 12"><path d="M5 11.5C2 7.5 1 6 1 4.5a4 4 0 0 1 8 0C9 6 8 7.5 5 11.5Z" fill="#fff"/><circle cx="5" cy="4.5" r="1.4" fill="#1f1f23"/></svg></span>
        <span>482 W. Harbor Avenue<br>Lakeview, Fl 33190</span>
      </li>
    </ul>
  </div>

  <div class="services">
    <div class="services__rule"></div>
    <div class="services__band">
      • New installations • Additions • Rewiring • Repairs<br>
      • Maintenance 24 hours • Faults and Emergency Assistance •
    </div>
    <div class="services__rule"></div>
  </div>
</section>

</body>
</html>
```